Meridian Systems Line Card

I need to create a one page line card that displays the services that my company provides and the certifications we hold.
I have an updated logo that I will post as soon as I get it later today. For now you can see an example at:
The new logo is very close to this and the colors are the same.
The file that I have posted is an example of what I think is a slick format. the upload is a two page document, but I really only like the first page. What I need a little bit of marketing and then room for the content that describes our core services and certifications.
The content of the line card needs to be divided into 9 categories:
Cloud (Virtual) Computing environments
Links are to our current brochures on these items for reference.
Greetings all,
Greetings everyone!
Small to Medium sized businesses as well as government institutions. This should be a one page "firm handshake" type exposure that tells the customer they are dealing with a first class professional operation.
It Company

```html
<!DOCTYPE html>
<html lang="en">
<head>
<meta charset="utf-8">
<title>Meridian Systems Line Card</title>
<link rel="stylesheet" href="https://fonts.googleapis.com/css2?family=Michroma&family=Open+Sans:wght@400;700&display=swap">
<style>
  :root {
    --paper: #e7b98a;
    --band: #d27c05;
    --ink: #1e1a15;
    --body-ink: #33281d;
    --box: #ffffff;
    --footer: #16110c;
    --accent: #d27c05;
  }
  html, body { margin: 0; padding: 0; overflow: hidden; }
  body { width: 848px; height: 1200px; background: var(--paper); font-family: "Open Sans", Arial, sans-serif; }
  .card { position: relative; width: 848px; height: 1200px; overflow: hidden; background: var(--paper); }

  .brand-mark { position: absolute; left: 62px; top: 66px; width: 156px; height: 156px; background: var(--accent); }
  .brand-name {
    position: absolute; left: 262px; top: 86px; margin: 0;
    font-family: "Michroma", Arial, sans-serif; font-weight: 400;
    font-size: 50px; line-height: 64px; letter-spacing: 1px; color: var(--ink);
  }
  .tagline {
    position: absolute; left: 380px; top: 206px; margin: 0;
    font-size: 17px; letter-spacing: 2px; color: var(--ink);
  }

  .service { position: absolute; left: 0; width: 848px; height: 70px; }
  .service-band { position: absolute; left: 0; top: 14px; width: 425px; height: 42px; background: var(--band); }
  .service-icon {
    position: absolute; left: 62px; top: 0; width: 60px; height: 60px;
    background: var(--box); border: 3px solid var(--ink); border-radius: 10px;
  }
  .service-title {
    position: absolute; left: 158px; top: 14px; height: 42px; margin: 0;
    display: flex; align-items: center;
    font-weight: 700; font-size: 28px; color: var(--ink); line-height: 1.05;
  }
  .service-title.small { font-size: 21px; }
  .service-text {
    position: absolute; left: 440px; top: -6px; width: 350px; margin: 0;
    font-size: 15.5px; line-height: 21px; color: var(--body-ink);
  }

  .footer { position: absolute; left: 0; top: 1117px; width: 640px; height: 38px; background: var(--footer); }
  .footer-url {
    position: absolute; left: 50px; top: 0; line-height: 38px; margin: 0;
    font-weight: 700; font-size: 20px; color: var(--accent);
  }
</style>
</head>
<body>
<main class="card">
  <header>
    <div class="brand-mark" aria-hidden="true"></div>
    <h1 class="brand-name">MERIDIAN<br>SYSTEMS.NET</h1>
    <p class="tagline">ENTERPRISE SOLUTIONS FOR EVERYONE</p>
  </header>

  <section class="service" style="top:255px">
    <div class="service-band"></div><div class="service-icon"></div>
    <h2 class="service-title">BDR</h2>
    <p class="service-text">Bulletproof your Data Protection with the Highest Industry Standards in an All-In-One Backup &amp; Business Continuity Solution</p>
  </section>

  <section class="service" style="top:345px">
    <div class="service-band"></div><div class="service-icon"></div>
    <h2 class="service-title small">Cloud (Virtual)<br>Computing enviroments</h2>
    <p class="service-text">Eliminate expensive start-up costs and IT management overhead with enterprise level cloud solutions.</p>
  </section>

  <section class="service" style="top:436px">
    <div class="service-band"></div><div class="service-icon"></div>
    <h2 class="service-title">Nimbus 365</h2>
    <p class="service-text">The reliability of Nimbus Office has now been enhanced with cloud features.</p>
  </section>

  <section class="service" style="top:526px">
    <div class="service-band"></div><div class="service-icon"></div>
    <h2 class="service-title">Outsourced IT</h2>
    <p class="service-text">Meridian Systems provides customized Proactive IT monitoring and support that</p>
  </section>

  <section class="service" style="top:616px">
    <div class="service-band"></div><div class="service-icon"></div>
    <h2 class="service-title">Network Security</h2>
    <p class="service-text">How secure is your network? Are you at risk? It´s time to get proactive!</p>
  </section>

  <section class="service" style="top:706px">
    <div class="service-band"></div><div class="service-icon"></div>
    <h2 class="service-title">Server Care</h2>
    <p class="service-text">Flat-Rate Managed Server Care is a complete, 24x7x365 server monitoring, remediation, maintenance and management solution.</p>
  </section>

  <section class="service" style="top:796px">
    <div class="service-band"></div><div class="service-icon"></div>
    <h2 class="service-title small">Desktop and user Care</h2>
    <p class="service-text">Proactive Maintenance and Security Updates for your Workstations, Remote and On-Site IT Support for your Staff</p>
  </section>

  <section class="service" style="top:886px">
    <div class="service-band"></div><div class="service-icon"></div>
    <h2 class="service-title">VOIP</h2>
    <p class="service-text">Businesses that utilize VoIP save money and gain more communication features. Make a Smart Investment with your Small Business by switching to VoIP.</p>
  </section>

  <section class="service" style="top:976px">
    <div class="service-band"></div><div class="service-icon"></div>
    <h2 class="service-title small" style="font-size:24px">Vendor management</h2>
    <p class="service-text">Get better, faster support for your third-party hardware and software investments and one point of contact for all of your vendor relationships.</p>
  </section>

  <footer class="footer">
    <p class="footer-url">www.meridiansystems.net</p>
  </footer>
</main>
</body>
</html>
```